Cultured Basics Website Design

We need a modern, elegant website for a nutritional product called "Cultured Basics" which is based on the diets of people living in Longevity Hot Spots. In Longevity Hot Spots people live uncommonly longer and healthier lives. Most of these Hot Spots are in exotic locations around the world. I have attached several images taken from the Hot Spot in Costa Rica, along with our Logo and the text for the entire website. It is not necessary to use/include all of the text, we can add and adjust that later. For now, we need the design for the home page and template for interior pages. You do not have to use the images we provide, we can purchase additional images if needed. "Final selection should include Adobe Muse template file and all supporting graphics in editable formats (PhotoShop, Illustrator, etc)" We have posted several projects on Sketch Harbor and have accepted in every case. We look forward to seeing your design for our website. Thanks!
We like the look of these websites as an example. You have to press "Preview" (which is located on the right) to see the website.
https://www.pagebloomer.com/websites/templates/drift
https://www.pagebloomer.com/websites/templates/marlow
35-60 80% female, 20% male
Product
1 page

```html
<!DOCTYPE html>
<html lang="en">
<head>
<meta charset="utf-8">
<title>Cultured Basics</title>
<link href="https://fonts.googleapis.com/css2?family=Open+Sans:wght@400;600;700;800&family=Kalam:wght@700&display=swap" rel="stylesheet">
<style>
:root{
  --green:#6ab42d;
  --green-soft:#cfe6b6;
  --dark:#3b3b3b;
  --darker:#2b2b2b;
  --ink:#333;
  --muted:#666;
  --line:#d9d9d9;
  --page:#ffffff;
  --strip:#e6e6e6;
}
*{box-sizing:border-box;margin:0;padding:0}
html,body{width:1200px;height:4027px;overflow:hidden;background:var(--page);font-family:"Open Sans",Arial,sans-serif;color:var(--ink)}
.canvas{position:relative;width:1200px;height:4027px}
.abs{position:absolute}
.photo{position:absolute}

/* header */
.topbar{left:182px;top:0;width:855px;height:102px;background:var(--dark)}
.brand{left:82px;top:16px;display:flex;align-items:center;gap:10px}
.brand-dot{width:30px;height:30px;border-radius:50%;background:var(--green)}
.brand-name{font-size:34px;font-weight:700;color:#fff;line-height:1}
.brand-tag{left:122px;top:60px;font-size:9px;color:#cfcfcf;letter-spacing:.5px}
.search{left:506px;top:19px;width:199px;height:32px;background:#fff;display:flex}
.search-btn{width:34px;height:32px;background:var(--green);display:flex;align-items:center;justify-content:center}
.search-field{flex:1;font-size:11px;color:#999;padding:8px}
.cart{left:716px;top:19px;display:flex;align-items:center;gap:8px;color:#ddd;font-size:11px}
.cart-btn{width:30px;height:32px;background:var(--green);display:flex;align-items:center;justify-content:center}
.account{left:518px;top:68px;display:flex;gap:20px;font-size:11px;color:#e3e3e3}
.nav{left:182px;top:102px;width:855px;height:51px;background:#fff;border-bottom:4px solid var(--green)}
.nav ul{position:absolute;left:82px;top:4px;display:flex;list-style:none}
.nav li{height:43px;border:1px solid var(--line);border-right:none;font-size:13px;font-weight:700;color:var(--ink);display:flex;align-items:center;justify-content:center}
.nav li:last-child{border-right:1px solid var(--line)}
.nav li.active{position:relative}
.nav .flag{position:absolute;top:-8px;left:50%;transform:translateX(-50%);background:var(--green);color:#fff;font-size:8px;padding:1px 6px}

/* hero */
.hero{left:182px;top:153px;width:855px;height:392px;background:linear-gradient(180deg,#6f6a6d 0%,#c89a82 40%,#7d7474 60%,#3e4144 100%)}
.hero-title{left:0;width:855px;top:160px;text-align:center;font-family:"Kalam",cursive;font-size:38px;line-height:44px;color:#fff}
.hero-title span{color:var(--green);display:block}
.dots{left:385px;top:333px;display:flex;gap:8px}
.dots i{width:14px;height:14px;border-radius:50%;background:#ddd;display:block}
.dots i.on{background:var(--green)}

/* story */
.story{left:182px;top:556px;width:855px;height:531px;background:linear-gradient(180deg,#c3d2e3 0%,#e6ecf2 45%,#9fb1b8 58%,#e9e4d8 72%,#fff 100%)}
.sec-title{font-size:27px;font-weight:800;color:var(--ink);text-align:center;width:855px;left:0}
.lead{font-size:11px;color:var(--green);font-weight:600;text-align:center;left:0;width:855px}
.body{font-size:10px;line-height:14px;color:#444;text-align:center}
.btn-outline{left:386px;top:218px;border:1px solid #444;font-size:10px;font-weight:700;padding:4px 8px;color:var(--ink)}
.divider{left:262px;top:1087px;width:694px;height:2px;background:var(--line)}

/* mission */
.mission{left:617px;top:1133px;width:419px;height:89px;background:var(--green-soft);padding:10px 22px}
.mission h2{font-size:24px;font-weight:800;color:var(--ink);line-height:26px}
.mission p{font-size:11px;line-height:14px;color:#3a6b1c;margin-top:3px}

.headline{left:0;width:1200px;text-align:center;font-size:30px;font-weight:700;color:var(--green)}
.para{left:262px;width:694px;text-align:center;font-size:11px;line-height:15px;color:#444}

/* footer */
.social{left:182px;top:3609px;width:855px;height:53px;background:var(--strip);display:flex;justify-content:center;align-items:center;gap:14px}
.social i{width:24px;height:24px;border-radius:50%;background:#444;display:block}
.footer{left:182px;top:3678px;width:855px;height:282px;background:var(--dark);color:#fff}
.foot-col h3{font-size:14px;font-weight:800;margin-bottom:8px}
.foot-col p,.foot-col li{font-size:11px;line-height:17px;list-style:none;color:#eee}
.field{width:185px;height:22px;border:1px solid #666;background:#4a4a4a;font-size:9px;color:#bbb;padding:4px 8px;margin-bottom:6px}
.field.tall{height:56px}
.send{left:188px;top:192px;width:54px;height:20px;background:var(--green);font-size:10px;font-weight:700;text-align:center;line-height:20px}
.copy{left:182px;top:3960px;width:855px;height:67px;background:var(--darker);color:#ddd;font-size:11px;padding:24px 36px}
</style>
</head>
<body>
<div class="canvas">

  <header>
    <div class="abs topbar">
      <div class="abs brand"><span class="brand-dot"></span><span class="brand-name">Cultured Basics</span></div>
      <div class="abs brand-tag">Naturally Enhanced Superfoods</div>
      <div class="abs search">
        <div class="search-btn"><svg width="16" height="16" viewBox="0 0 16 16"><circle cx="6.5" cy="6.5" r="4.5" fill="none" stroke="#fff" stroke-width="2"/><line x1="10" y1="10" x2="14" y2="14" stroke="#fff" stroke-width="2"/></svg></div>
        <div class="search-field">Search...</div>
      </div>
      <div class="abs cart">
        <div class="cart-btn"><svg width="16" height="14" viewBox="0 0 16 14"><path d="M1 1h3l2 8h8l1-6H5" fill="none" stroke="#fff" stroke-width="1.6"/><circle cx="7" cy="12" r="1.3" fill="#fff"/><circle cx="13" cy="12" r="1.3" fill="#fff"/></svg></div>
        <span>Your cart</span>
      </div>
      <div class="abs account"><span>Compare</span><span>Wishlist</span><span>Help</span><span>Register</span><span>Login</span></div>
    </div>
    <nav class="abs nav">
      <ul>
        <li style="width:82px">HOME</li>
        <li style="width:87px">STORY</li>
        <li class="active" style="width:95px"><span class="flag">NEW</span>PRODUCT</li>
        <li style="width:185px">HOW TO TAKE FERMENTED</li>
        <li style="width:120px">OUR MISSION</li>
        <li style="width:112px">GALLERY</li>
      </ul>
    </nav>
  </header>

  <section class="abs hero" role="img" aria-label="Wooden boat on a beach at sunset">
    <div class="abs hero-title">Naturally Enhanced<span>Superfoods</span></div>
    <div class="abs dots"><i></i><i class="on"></i><i></i><i></i></div>
  </section>

  <section class="abs story" role="img" aria-label="Palm trees and a calm tropical beach under a pale sky">
    <h2 class="abs sec-title" style="top:66px">STORY</h2>
    <p class="abs lead" style="top:104px">Cultured Basics Story - Read to know the path toward longevity for life and core figures</p>
    <p class="abs body" style="left:225px;width:405px;top:124px">It was in 2004 that wellness founder Daniel Reyes first came to a small village on the Nicoya coast, where families share an exceptional record of long lives. Living among them, he studied their meals, habits and daily rhythm, and slowly the pattern became clear. The findings have since been shared widely by health writers and researchers.</p>
    <div class="abs btn-outline">READ MORE</div>
    <h2 class="abs sec-title" style="top:382px">VISION</h2>
    <p class="abs lead" style="top:428px">A world away, there's a lifetime of good health to be discovered.</p>
    <p class="abs body" style="left:100px;width:655px;top:452px">In remote corners of the world, across the globe and for thousands of years, a handful of cultures have mastered the art of living well. In these few places, people stay active and happy into their later years, and we believe simple, shared traditions can bring that same vitality to every home.</p>
  </section>
  <div class="abs divider"></div>

  <div class="photo" style="left:182px;top:1133px;width:427px;height:403px;background:linear-gradient(160deg,#5d6b3e,#8a7b5e 60%,#4e4a3b)" role="img" aria-label="Child walking through dry branches near a village"></div>
  <div class="abs mission">
    <h2>MISSION</h2>
    <p>Our mission is to have a profound impact on your health and wellness by helping you easily enjoy the fermented superfoods enjoyed by the world's healthiest people.</p>
  </div>
  <div class="photo" style="left:617px;top:1230px;width:419px;height:306px;background:linear-gradient(170deg,#7d8a5a,#a38a72 50%,#6b5d48)" role="img" aria-label="Two young women sitting on a bench outdoors"></div>

  <div class="photo" style="left:182px;top:1547px;width:854px;height:547px;background:linear-gradient(180deg,#2f7d6e 0%,#3d8b7a 45%,#8b7a6a 75%,#fff 100%)" role="img" aria-label="Family gathered on the porch of a teal house"></div>

  <h2 class="abs headline" style="top:2145px">What's in a name?</h2>
  <p class="abs para" style="top:2198px">In studying the healthiest people on earth we unearthed a truly amazing discovery. We found that these people consume a great deal of fermented foods. In fact, they consume a fermented food with nearly every meal. Fermented foods are nature's gift, a treasure from nature like nothing else. Truly Essential.</p>

  <div class="photo" style="left:182px;top:2277px;width:854px;height:362px;background:linear-gradient(180deg,#c8ccd0 0%,#a9adb0 30%,#7f8f93 48%,#8d8f8c 65%,#5d5f5c 100%)" role="img" aria-label="Two children playing in the surf on a wide beach"></div>

  <h2 class="abs headline" style="top:2685px">Your journey begins now.</h2>
  <p class="abs para" style="top:2735px">Thousands of people around the world live happier, healthier, more vibrant lives because of the simple choices they make each and every day. You can too. Make a commitment today to embrace the types of foods enjoyed by the healthiest people on earth and sorely missing in most modern diets.<br>Become inspired and empowered, improve the way you live, share your wellness journey with others, and secure a healthy, rewarding future for years to come.</p>

  <div class="photo" style="left:182px;top:2868px;width:427px;height:359px;background:linear-gradient(170deg,#4f6b3a,#a8a397 55%,#6a5c44)" role="img" aria-label="Old wooden boat resting on sand under palms"></div>
  <div class="photo" style="left:617px;top:2868px;width:419px;height:235px;background:linear-gradient(180deg,#cfd6dc,#93aab2 50%,#5f7a45)" role="img" aria-label="Bay view with palm trees and green shrubs"></div>
  <div class="photo" style="left:182px;top:3235px;width:476px;height:315px;background:linear-gradient(160deg,#6b8a45,#c7a27a 50%,#5a8a4e)" role="img" aria-label="Woman in a sun hat standing with an elderly man in a garden"></div>
  <div class="photo" style="left:666px;top:3110px;width:370px;height:440px;background:linear-gradient(170deg,#4d7a3a,#6fb3c8 45%,#9b7a5e 70%,#5a9a4a)" role="img" aria-label="Elderly man and woman in a sun hat beside a pool"></div>

  <div class="abs social" aria-label="Social links"><i></i><i></i><i></i></div>

  <footer class="abs footer">
    <div class="abs foot-col" style="left:36px;top:26px">
      <h3>QUICK LINKS</h3>
      <ul><li>Home</li><li>About</li><li>Product Range</li><li>Product Review</li><li>Services</li><li>Info</li></ul>
    </div>
    <div class="abs foot-col" style="left:196px;top:26px">
      <h3>LOCATIONS</h3>
      <p>14 Maple St, Ashbury<br>Western Australia 6109</p>
      <p style="margin-top:8px">PH 555-0142<br>info@culturedbasics.com</p>
    </div>
    <div class="abs foot-col" style="left:392px;top:26px;width:260px;height:230px">
      <h3>QUICK CONTACT</h3>
      <div class="field">Name</div>
      <div class="field">Email</div>
      <div class="field tall">Message</div>
      <div class="abs send">SEND</div>
    </div>
    <div class="abs foot-col" style="left:626px;top:20px;width:200px">
      <div style="display:flex;align-items:center;gap:8px"><span class="brand-dot" style="width:24px;height:24px"></span><span style="font-size:24px;font-weight:700;line-height:1">Cultured Basics</span></div>
      <p style="margin-top:26px;font-size:11px;line-height:15px">Lorem Ipsum is simply dummy text of the printing and typesetting industry. Lorem Ipsum has been the industry's standard dummy text ever since the 1500s, when an unknown printer took a galley of type and scrambled it to make a type specimen book.</p>
    </div>
  </footer>
  <div class="abs copy">Copyrights 2016 Ridgeline Tools WA. All Rights Reserved.</div>

</div>
</body>
</html>
```